Accountability Project Graphics

I want to create 10 social media graphics (new Instagram size 4:5 (1080 x 1350 pixels) focusing on our Quenral Accountability App, using any of the 3 pictures attached. Use the attached pics only, NO RANDOM STOCK PHOTOGRAPHY. For the color scheme, use the landing page colors/fonts (attached).
You can add any of the 3 photos attached but I mainly need BOLD text that includes these headlines and sub-headlines on them.
Please NOTE for all the headlines below, also add this sub-headline on each graphic:
Stay Consistent with RB in Your Pocket!
Here are the headlines:
• Stop Starting Over Every Monday
• You don't need more willpower. You need more support
• Built for women who are tired of doing this alone
• When Motivation Fades, RB Checks In
• The Support System You've Been Missing
• Support When Motivation Disappears
• What if RB Checked in Every Day?
• The Missing Piece Isn't Another Diet
• Eat the food you love. Stay accountable every day.
• One Bad Meal Doesn't Mean You Failed
Target Market(s)
women over 40 trying to lose weight
Look and feel
Each slider illustrates characteristics of the customer's brand and the style your logo design should communicate.

```html
<!DOCTYPE html>
<html lang="en">
<head>
<meta charset="utf-8">
<title>Quenral Accountability App – Social Graphics</title>
<link rel="stylesheet" href="https://fonts.googleapis.com/css2?family=Bebas+Neue&family=Inter:ital,wght@1,700&display=swap">
<style>
  :root {
    --plum: #2e1240;
    --rose: #d4497f;
    --blush-top: #f9dbe5;
    --blush-bottom: #fffafc;
    --board: #707070;
    --photo-dark: #2a2238;
    --photo-mid: #5a4560;
    --photo-warm: #c98aa3;
  }
  * { margin: 0; padding: 0; box-sizing: border-box; }
  html, body { width: 1200px; height: 1120px; overflow: hidden; background: var(--board); }
  .board { position: relative; width: 1200px; height: 1120px; }
  .post {
    position: absolute; width: 285px; height: 356px; overflow: hidden;
    background: linear-gradient(180deg, var(--blush-top) 0%, var(--blush-bottom) 100%);
  }
  .photo {
    position: absolute; z-index: 1; border-radius: 40% 40% 0 0 / 18% 18% 0 0;
    background: linear-gradient(180deg, var(--photo-mid) 0%, var(--photo-dark) 70%);
    opacity: .9;
  }
  .photo--pair { background: linear-gradient(180deg, var(--photo-mid) 0%, #4a6180 60%, #e9eef2 100%); }
  .photo--hug { background: linear-gradient(160deg, var(--photo-dark) 0%, var(--photo-warm) 55%, #e8f3d6 100%); }
  .photo--scene { border-radius: 0; }
  .headline {
    position: absolute; z-index: 2;
    font-family: "Bebas Neue", "Oswald", sans-serif;
    line-height: .86; color: var(--plum); text-transform: uppercase;
  }
  .headline span { display: block; }
  .headline .rose { color: var(--rose); }
  .headline--right { text-align: right; }
  .headline--center { text-align: center; left: 0; right: 0; }
  .tagline {
    position: absolute; z-index: 3; border-radius: 3px;
    font-family: "Inter", sans-serif; font-style: italic; font-weight: 700;
    font-size: 9.5px; line-height: 1.2; letter-spacing: -.1px; color: #fff;
    padding: 3px 9px; white-space: nowrap;
    background: var(--plum);
  }
  .tagline--rose { background: var(--rose); }
  .tagline--single { text-align: center; }
</style>
</head>
<body>
<div class="board">

  <!-- 1 -->
  <section class="post" style="left:10px;top:11px">
    <div class="photo photo--hug" style="left:129px;top:161px;width:154px;height:195px" role="img" aria-label="Photo of two women hugging and laughing"></div>
    <h2 class="headline" style="left:19px;top:16px">
      <span class="rose" style="font-size:37px">You</span>
      <span class="rose" style="font-size:37px">Don't need</span>
      <span class="rose" style="font-size:52px">More</span>
      <span class="rose" style="font-size:43px">Willpower.</span>
      <span style="font-size:39px">You</span>
      <span style="font-size:39px">Need</span>
      <span style="font-size:52px">More</span>
      <span style="font-size:39px">Support</span>
    </h2>
    <p class="tagline" style="left:20px;top:311px">Stay Consistent with RB<br>in Your Pocket!</p>
  </section>

  <!-- 2 -->
  <section class="post" style="left:308px;top:11px">
    <div class="photo" style="left:159px;top:86px;width:125px;height:270px" role="img" aria-label="Photo of the coach smiling, hand on hip, in a black lace top"></div>
    <h2 class="headline" style="left:22px;top:22px">
      <span style="font-size:90px">Stop</span>
      <span class="rose" style="font-size:46px">Starting</span>
      <span class="rose" style="font-size:73px">Over</span>
      <span style="font-size:63px">Every</span>
      <span style="font-size:52px">Monday</span>
    </h2>
    <p class="tagline" style="left:21px;top:302px">Stay Consistent with RB<br>in Your Pocket!</p>
  </section>

  <!-- 3 -->
  <section class="post" style="left:606px;top:11px">
    <div class="photo photo--pair" style="left:8px;top:155px;width:171px;height:201px" role="img" aria-label="Photo of two women laughing together"></div>
    <h2 class="headline headline--right" style="right:18px;top:21px">
      <span style="font-size:56px">The Missing</span>
      <span style="font-size:97px">Piece</span>
      <span style="font-size:66px">Isn't</span>
      <span class="rose" style="font-size:46px">Another</span>
      <span class="rose" style="font-size:60px">Diet</span>
    </h2>
    <p class="tagline tagline--rose" style="left:124px;top:304px">Stay Consistent with RB<br>in Your Pocket!</p>
  </section>

  <!-- 4 -->
  <section class="post" style="left:904px;top:11px">
    <div class="photo photo--scene" style="left:109px;top:0;width:176px;height:356px;background:linear-gradient(90deg,rgba(249,219,229,0) 0%,#8a5a4c 25%,var(--photo-dark) 55%,#b9a6aa 100%)" role="img" aria-label="Photo of the coach standing by a pool table in a lounge"></div>
    <h2 class="headline" style="left:18px;top:14px;line-height:.84">
      <span style="font-size:39px">Built for</span>
      <span style="font-size:49px">Women</span>
      <span style="font-size:39px">Who are</span>
      <span style="font-size:41px">Tired of</span>
      <span class="rose" style="font-size:56px">Doing</span>
      <span class="rose" style="font-size:76px">This</span>
      <span class="rose" style="font-size:54px">Alone</span>
    </h2>
    <p class="tagline tagline--rose" style="left:13px;top:312px">Stay Consistent with RB<br>in Your Pocket!</p>
  </section>

  <!-- 5 -->
  <section class="post" style="left:10px;top:385px">
    <div class="photo photo--hug" style="left:80px;top:25px;width:133px;height:161px" role="img" aria-label="Photo of two women hugging and laughing"></div>
    <h2 class="headline headline--center" style="top:180px;line-height:.8">
      <span class="rose" style="font-size:46px">Support when</span>
      <span style="font-size:60px">Motivation</span>
      <span style="font-size:54px">Disappears</span>
    </h2>
    <p class="tagline tagline--single" style="left:27px;top:314px;width:229px">Stay Consistent with RB in Your Pocket!</p>
  </section>

  <!-- 6 -->
  <section class="post" style="left:308px;top:385px">
    <div class="photo" style="left:10px;top:136px;width:140px;height:220px" role="img" aria-label="Photo of the coach smiling, hand on hip, in a black lace top"></div>
    <h2 class="headline headline--right" style="right:19px;top:28px">
      <span style="font-size:52px">The Support</span>
      <span style="font-size:69px">System</span>
      <span class="rose" style="font-size:63px">You've</span>
      <span class="rose" style="font-size:52px">Been</span>
      <span class="rose" style="font-size:54px">Missing</span>
    </h2>
    <p class="tagline tagline--rose" style="left:125px;top:277px">Stay Consistent with RB<br>in Your Pocket!</p>
  </section>

  <!-- 7 -->
  <section class="post" style="left:606px;top:385px">
    <div class="photo photo--pair" style="left:109px;top:156px;width:166px;height:200px" role="img" aria-label="Photo of two women laughing together"></div>
    <h2 class="headline" style="left:23px;top:16px">
      <span style="font-size:73px">What if</span>
      <span style="font-size:49px">RB Checked</span>
      <span class="rose" style="font-size:84px">In</span>
      <span class="rose" style="font-size:60px">Every</span>
      <span class="rose" style="font-size:64px">Day?</span>
    </h2>
    <p class="tagline tagline--rose" style="left:21px;top:312px">Stay Consistent with RB<br>in Your Pocket!</p>
  </section>

  <!-- 8 -->
  <section class="post" style="left:904px;top:385px">
    <div class="photo photo--scene" style="left:0;top:0;width:175px;height:356px;background:linear-gradient(90deg,#8a5a4c 0%,var(--photo-dark) 45%,rgba(249,219,229,0) 100%)" role="img" aria-label="Photo of the coach leaning on a pool table in a lounge"></div>
    <h2 class="headline" style="left:141px;top:14px">
      <span class="rose" style="font-size:43px">One bad</span>
      <span class="rose" style="font-size:67px">Meal</span>
      <span style="font-size:43px">Doesn't</span>
      <span style="font-size:69px">Mean</span>
      <span class="rose" style="font-size:63px">You</span>
      <span class="rose" style="font-size:60px">Failed</span>
    </h2>
    <p class="tagline tagline--rose" style="left:139px;top:312px">Stay Consistent with RB<br>in Your Pocket!</p>
  </section>

  <!-- 9 -->
  <section class="post" style="left:308px;top:753px">
    <div class="photo" style="left:159px;top:86px;width:125px;height:270px" role="img" aria-label="Photo of the coach smiling, hand on hip, in a black lace top"></div>
    <h2 class="headline" style="left:22px;top:22px;width:132px">
      <span style="font-size:69px">When</span>
      <span style="font-size:32px">Motivation</span>
      <span style="font-size:60px">Fades,</span>
      <span class="rose" style="font-size:105px;text-align:center">RB</span>
      <span class="rose" style="font-size:39px">Checks in</span>
    </h2>
    <p class="tagline tagline--rose" style="left:21px;top:304px">Stay Consistent with RB<br>in Your Pocket!</p>
  </section>

  <!-- 10 -->
  <section class="post" style="left:606px;top:753px">
    <h2 class="headline headline--center" style="top:24px">
      <span class="rose" style="font-size:50px">Eat the food</span>
      <span class="rose" style="font-size:66px">You love.</span>
      <span style="font-size:78px">Stay</span>
      <span style="font-size:49px">Accountable</span>
      <span style="font-size:59px">Every day.</span>
    </h2>
    <p class="tagline tagline--single" style="left:26px;top:310px;width:233px">Stay Consistent with RB in Your Pocket!</p>
  </section>

</div>
</body>
</html>
```